Business Card - Self Employed Director

My husband needs a business card design. 2 sided printing required.

He is self employed, in the vineyard management and renewable energy sectors (see below for more information) and design and accent colors should reflect this.

Design should be modern but classic and professional too.

Card to show personal contact information only. Exact information subject to confirmation on finalizing design as we are moving soon and need to confirm the exact details.

Dorian Feltsworth
email: dorian.feltsworth@brenquaystone.com
mobile: 021 064 51837
home: +64 (0) 3 4182 615
147 Harrow Fern Rise, RD4 Pellingham, Marlborough, NZ 7271

I like the attached design by Vexo for inspiration.

The reverse side should show name in bottom right corner with the pattern possibly reflecting renewable energy? Waves? Wind? Sea green, teal? Fresh, clean
Image on reverse should not be a photograph but a clean graphic based print on white background. Sans serfic fonts, Charcoal grey not black with accent colors reflected on the back?

Print ready artwork will be required. Please ask any questions :-) THANKS

Industry/Entity Type

Printing

Font styles to use
Sans Serif

Colors
86cfc6
ffffff
85abd2

Requirements
Must have
• Contact information as show
Should not have
• Anything cute, no red. No fancy flourish fonts.

```html
<!DOCTYPE html>
<html lang="en">
<head>
<meta charset="utf-8">
<title>Dorian Feltsworth – Business Card</title>
<link rel="stylesheet" href="https://fonts.googleapis.com/css2?family=Source+Sans+3:wght@400;700&display=swap">
<style>
  :root {
    --backdrop: #e9e6e1;
    --card-white: #ffffff;
    --charcoal: #3a3836;
    --teal: #62d0c4;
    --periwinkle: #8189de;
    --shadow: rgba(0, 0, 0, 0.16);
  }
  * { box-sizing: border-box; margin: 0; padding: 0; }
  html, body {
    width: 1200px;
    height: 900px;
    overflow: hidden;
    background: var(--backdrop);
    font-family: "Source Sans 3", Arial, sans-serif;
  }
  .sheet {
    position: relative;
    width: 1200px;
    height: 900px;
  }
  .card {
    position: absolute;
    left: 270px;
    width: 660px;
    height: 377px;
    overflow: hidden;
    background: var(--card-white);
    color: var(--charcoal);
    box-shadow: 0 8px 22px var(--shadow);
  }
  .card--front { top: 53px; }
  .card--back { top: 470px; }
  .name strong { font-weight: 700; }
  .name span { font-weight: 400; }

  /* Front */
  .front-foliage {
    position: absolute;
    left: 0;
    bottom: 0;
    width: 230px;
    height: 220px;
    background:
      radial-gradient(ellipse at 30% 95%, rgba(129, 137, 222, 0.40) 0%, rgba(129, 137, 222, 0.12) 45%, rgba(255,255,255,0) 70%),
      radial-gradient(ellipse at 75% 100%, rgba(98, 208, 196, 0.65) 0%, rgba(98, 208, 196, 0.22) 40%, rgba(255,255,255,0) 68%);
  }
  .contact {
    position: absolute;
    right: 30px;
    top: 140px;
    text-align: right;
    font-size: 17px;
    line-height: 1.3;
  }
  .contact .name { font-size: 19px; margin-bottom: 24px; }
  .contact .address { margin-bottom: 20px; }
  .contact .phones { margin-bottom: 20px; }

  /* Back */
  .back-name {
    position: absolute;
    left: 0;
    right: 0;
    top: 150px;
    text-align: center;
    font-size: 36px;
    line-height: 1.2;
  }
  .back-foliage {
    position: absolute;
    left: 0;
    right: 0;
    bottom: 0;
    height: 150px;
    background: linear-gradient(90deg, var(--periwinkle) 0%, var(--teal) 18%, var(--periwinkle) 32%, var(--teal) 50%, var(--periwinkle) 68%, var(--teal) 84%, var(--teal) 100%);
    -webkit-mask-image: linear-gradient(to top, rgba(0,0,0,0.75) 40%, rgba(0,0,0,0.25) 80%, transparent 100%);
            mask-image: linear-gradient(to top, rgba(0,0,0,0.75) 40%, rgba(0,0,0,0.25) 80%, transparent 100%);
  }
</style>
</head>
<body>
  <main class="sheet">
    <section class="card card--front">
      <div class="front-foliage" role="img" aria-label="Leafy sprigs illustration in periwinkle outline and teal silhouette"></div>
      <div class="contact">
        <p class="name"><strong>Dorian</strong> <span>Feltsworth</span></p>
        <p class="address">147 Harrow Fern Rise,<br>RD4 Pellingham, Marlborough, NZ 7271</p>
        <p class="phones">M: 021 064 51837<br>T: +64 (0) 3 4182 615</p>
        <p class="email">E: dorian.feltsworth@brenquaystone.com</p>
      </div>
    </section>

    <section class="card card--back">
      <p class="back-name name"><strong>Dorian</strong> <span>Feltsworth</span></p>
      <div class="back-foliage" role="img" aria-label="Row of leafy sprigs in alternating teal and periwinkle along the bottom edge"></div>
    </section>
  </main>
</body>
</html>
```